Logo is done, need templates now

I want to be able to have an email template, same for word documents, powerpoint etc. I have the logo, now I need all the pieces for appearance in correspondence and marketing

Target Market(s)

Professional Advisors and Wealthy Clients

Font styles to use
Serif

Requirements
Must have
• I want to be able to do word documents and email them with letterhead. I need great email signatures. I need similar formatting for the word documents to be flexible to add to powerpoint and other presentations.

```html
<!DOCTYPE html>
<html lang="en">
<head>
<meta charset="utf-8">
<title>Marlow Reserve — Letterhead Header</title>
<link href="https://fonts.googleapis.com/css2?family=Cormorant+Garamond:wght@500&display=swap" rel="stylesheet">
<style>
  :root {
    --page: #ffffff;
    --band: #2e2e2d;
    --band-accent: #424242;
    --gold: #b8955f;
  }
  html, body {
    margin: 0;
    padding: 0;
    width: 1200px;
    height: 139px;
    overflow: hidden;
    background: var(--page);
  }
  .letterhead {
    position: relative;
    width: 1200px;
    height: 139px;
  }
  .header-band {
    position: absolute;
    left: 245px;
    top: 0;
    width: 751px;
    height: 126px;
    background: var(--band);
    border-radius: 0 0 37px 37px;
    overflow: hidden;
  }
  .band-emblem {
    position: absolute;
    left: 345px;
    top: -95px;
    width: 260px;
    height: 260px;
    border-radius: 50%;
    background: var(--band-accent);
  }
  .brand-lockup {
    position: absolute;
    left: 0;
    top: 38px;
    width: 296px;
    display: flex;
    flex-direction: column;
    align-items: center;
  }
  .brand-square {
    width: 40px;
    height: 40px;
    background: var(--gold);
  }
  .brand-name {
    margin: 12px 0 0;
    padding-left: 0.24em;
    font-family: "Cormorant Garamond", Georgia, serif;
    font-weight: 500;
    font-size: 20px;
    line-height: 1;
    letter-spacing: 0.24em;
    color: var(--gold);
    text-transform: uppercase;
    white-space: nowrap;
  }
</style>
</head>
<body>
  <header class="letterhead">
    <div class="header-band">
      <div class="band-emblem" aria-hidden="true"></div>
      <div class="brand-lockup">
        <div class="brand-square" aria-hidden="true"></div>
        <p class="brand-name">Marlow Reserve</p>
      </div>
    </div>
  </header>
</body>
</html>
```